ReDesign Website for a more Bold approach

Hello! I'd like to redesign my website: torvellacapital.com

I'd like to add one thing that's not on my website which is a blog. The design around the blog should be put time into as I will be putting out incredibly great content and want it to attract viewers.

I get a lot of inspiration from quondel.com (the way they flow the big statements across each screen, colors)
amberlit.vc (the simplicity behind the design is beautiful)

I like modern very simple but bold approaches.

I am going to attach my logo here and if it can be thought of when making the design of the website. Thanks!

Industry/Entity Type

Finance and Private Equity

Number of Pages Required

3 page

Font styles to use
Serif
Sans Serif

Colors
0054AA
0677BA
7BADD7
CADEEF
E8F1F8
0094D4
00A9DD
6FCCEA
C7EBF8
E9F6FB
00AB8E
00BBA5
67D7C9
C6EFE9
E9F9F6

Requirements
Must have
• My project must have a Home, Expertise, Story, Clients, Approach, Blog, Contact
Nice to have
• It would be nice to have these tabs reduced to 1-3 pages
Should not have
• My project must not have bright colors.

```html
<!DOCTYPE html>
<html lang="en">
<head>
<meta charset="utf-8">
<title>Torvella Capital</title>
<link href="https://fonts.googleapis.com/css2?family=Playfair+Display:wght@400&family=Mulish:wght@400;600;700;800&family=Montserrat:wght@700&display=swap" rel="stylesheet">
<style>
:root{
  --navy:#0c2542;
  --blue-deep:#0054aa;
  --blue:#0677ba;
  --blue-soft:#7badd7;
  --blue-pale:#e8f4fb;
  --sky:#0094d4;
  --sky-bright:#00a9dd;
  --sky-soft:#6fccea;
  --teal:#00bba5;
  --teal-band:#33bfa8;
  --teal-soft:#67d7c9;
  --form-bg:#2f74bf;
  --text:#555a60;
  --white:#ffffff;
}
*{box-sizing:border-box;margin:0;padding:0}
html,body{width:1200px;height:3900px;overflow:hidden}
body{font-family:'Mulish',sans-serif;color:var(--text);position:relative;background:var(--white)}
section,header{position:absolute;left:0;width:1200px}
.abs{position:absolute}
.serif{font-family:'Playfair Display',serif;font-weight:400}

/* header */
.site-header{top:0;height:68px;background:var(--navy)}
.brand{left:87px;top:22px;font-family:'Montserrat',sans-serif;font-weight:700;font-size:19px;color:var(--white);letter-spacing:.3px}
.main-nav a{position:absolute;top:25px;font-size:13px;color:var(--white);text-decoration:none}
.dropdown{left:926px;top:68px;width:209px;height:177px;background:rgba(123,173,215,.92);z-index:3}
.dropdown a{display:block;height:35px;padding-left:18px;line-height:35px;font-size:12.5px;color:var(--white);text-decoration:none}
.dropdown a:first-child{margin-top:2px}

/* hero */
.hero{top:68px;height:474px;background:linear-gradient(180deg,#2f7fc4 0%,#2a78bd 55%,#3f86c4 100%)}
.hero-kicker{top:150px;width:100%;text-align:center;font-size:21px;color:var(--teal-soft)}
.hero-title{top:182px;width:100%;text-align:center;font-size:46px;line-height:53px;color:var(--white);text-shadow:0 2px 6px rgba(0,0,0,.35)}
.link-cta{font-weight:800;color:var(--teal-soft);text-decoration:none;border-bottom:3px solid var(--teal-soft);padding-bottom:1px}
.hero-cta{top:341px;width:100%;text-align:center;font-size:20px}
.hero-chevron{left:585px;top:398px}

/* stats */
.stats{top:542px;height:293px;background:var(--teal)}
.stat{position:absolute;top:65px;width:260px;text-align:center;color:var(--white)}
.stat svg{display:block;margin:0 auto}
.stat-num{font-size:38px;font-weight:800;line-height:40px;margin-top:18px}
.stat-label{font-size:17px;font-weight:600;margin-top:2px}

/* expertise */
.expertise{top:835px;height:528px}
.panel-pale{background:var(--blue-pale)}
.expertise-panel{left:0;top:0;width:496px;height:528px}
.big-title{font-size:52px;line-height:58px;color:var(--blue)}
.expertise .big-title{left:177px;top:183px}
.service{position:absolute;width:250px}
.service h3{font-size:15px;font-weight:800;color:var(--sky);letter-spacing:.2px;margin-bottom:12px}
.service p{font-size:13px;line-height:23px}

/* who */
.who{top:1363px;height:528px;background:linear-gradient(135deg,#86b4da 0%,#9ec2e2 45%,#8ab7dc 100%)}
.who h2{top:52px;width:100%;text-align:center;font-size:50px;color:var(--white)}
.who-copy{left:129px;top:158px;width:943px;font-size:13px;line-height:23px;color:var(--white)}
.who-copy p{margin-bottom:22px}
.who-cta{top:436px;width:100%;text-align:center;font-size:20px}

/* approach */
.approach{top:1891px;height:527px}
.approach-panel{left:705px;top:0;width:495px;height:527px}
.approach .big-title{left:823px;top:200px;color:var(--blue-deep)}
.approach-copy{left:86px;top:62px;width:535px;font-size:13px;line-height:23px}
.approach-copy p{margin-bottom:22px}
.approach-cta{left:87px;top:442px;font-size:21px;font-weight:800;color:var(--blue);text-decoration:none;border-bottom:4px solid var(--sky-soft)}

/* clients */
.clients{top:2418px;height:354px;background:var(--teal-band)}
.clients h2{top:52px;width:100%;text-align:center;font-size:52px;color:var(--white)}
.client{position:absolute;width:150px;text-align:center;font-size:22px;font-weight:700;color:var(--white);display:flex;align-items:center;justify-content:center;gap:7px}
.client i{display:inline-block;width:12px;height:12px;border-radius:50%;background:var(--white)}

/* news */
.news{top:2772px;height:431px}
.news h2{top:52px;width:100%;text-align:center;font-size:52px;color:var(--blue)}
.post{position:absolute;top:138px;width:320px}
.post h3{font-size:17px;font-weight:600;line-height:21px;color:var(--sky)}
.post-meta{margin-top:12px;font-size:12px;color:var(--blue-soft);word-spacing:1px}
.post-meta span{margin-left:28px}
.post p{margin-top:12px;font-size:13px;line-height:23px}
.read-more{display:inline-block;margin-top:4px;margin-left:4px;font-size:14px;color:var(--text);text-decoration:none;border-bottom:3px solid var(--teal-soft);line-height:14px}

/* newsletter */
.newsletter{top:3203px;height:236px;background:var(--blue-soft)}
.newsletter h2{top:42px;width:100%;text-align:center;font-size:34px;color:var(--white)}
.newsletter h3{top:88px;width:100%;text-align:center;font-size:26px;color:var(--white)}
.field{position:absolute;background:var(--white);border:0;font-family:'Mulish',sans-serif;font-size:12px;color:var(--blue-soft);padding:0 10px;display:flex;align-items:center}
.btn{position:absolute;color:var(--white);font-size:13px;display:flex;align-items:center;justify-content:center}

/* contact */
.contact{top:3439px;height:461px;background:var(--form-bg)}
.contact h2{top:52px;width:100%;text-align:center;font-size:48px;color:var(--sky-soft)}
.contact-intro{top:128px;width:100%;text-align:center;font-size:13px;line-height:23px;color:var(--white)}
.footer-rule{left:236px;top:388px;width:726px;height:1px;background:var(--blue-soft)}
.copyright{left:260px;top:421px;font-size:13px;color:var(--blue-soft)}
.social{position:absolute;top:415px;width:26px;height:26px;border-radius:50%;background:var(--blue-soft)}
</style>
</head>
<body>

<header class="site-header">
  <div class="abs brand">TORVELLA CAPITAL</div>
  <nav class="main-nav">
    <a style="left:843px">HOME</a>
    <a style="left:932px">ABOUT US</a>
    <a style="left:1049px">CONTACT</a>
  </nav>
</header>

<nav class="abs dropdown" aria-label="About us">
  <a>Area of Expertise</a><a>Our Story</a><a>Our Approach</a><a>Our Clients</a><a>Blog</a>
</nav>

<section class="hero" role="img" aria-label="City skyline with construction cranes under a blue tint">
  <p class="abs hero-kicker">Torvella Capital is a venture capital studio firm</p>
  <h1 class="abs serif hero-title">Raising solid capital for startups and<br>helping businesses jumpstart their revenue</h1>
  <div class="abs hero-cta"><a class="link-cta">Find Out More</a></div>
  <svg class="abs hero-chevron" width="30" height="20" viewBox="0 0 30 20"><path d="M3 3l12 12L27 3" fill="none" stroke="#fff" stroke-width="4" stroke-linecap="round" stroke-linejoin="round"/></svg>
</section>

<section class="stats">
  <div class="stat" style="left:74px">
    <svg width="72" height="72" viewBox="0 0 72 72" fill="none" stroke="#fff" stroke-width="2.2" stroke-linejoin="round"><path d="M26 14h16l-4 8H30z"/><path d="M30 22c-14 8-20 22-16 32 2 6 10 8 20 8h8"/><path d="M38 22c8 5 12 12 14 18"/><text x="26" y="52" fill="#fff" stroke="none" font-family="Mulish" font-weight="700" font-size="20">$</text><rect x="44" y="44" width="20" height="5" rx="2"/><rect x="44" y="50" width="20" height="5" rx="2"/><rect x="44" y="56" width="20" height="5" rx="2"/><rect x="44" y="38" width="20" height="5" rx="2"/></svg>
    <div class="stat-num">$40M+</div><div class="stat-label">MONEY RAISED</div>
  </div>
  <div class="stat" style="left:339px">
    <svg width="72" height="72" viewBox="0 0 72 72" fill="none" stroke="#fff" stroke-width="2.2"><circle cx="20" cy="18" r="12"/><text x="15" y="24" fill="#fff" stroke="none" font-family="Mulish" font-weight="700" font-size="17">$</text><rect x="22" y="50" width="7" height="16"/><rect x="33" y="40" width="7" height="26"/><rect x="44" y="30" width="7" height="36"/><rect x="55" y="18" width="7" height="48"/><path d="M14 50l14-10 10 4 22-30"/><path d="M52 12h9v9"/></svg>
    <div class="stat-num">$125M+</div><div class="stat-label">ATTRIBUTED REVENUE</div>
  </div>
  <div class="stat" style="left:604px">
    <svg width="72" height="72" viewBox="0 0 72 72" fill="none" stroke="#fff" stroke-width="2.2" stroke-linejoin="round"><path d="M4 26l12-8 10 4 8-2 8 4"/><path d="M68 26l-12-8-14 6-10 8c-2 2 0 5 3 4l9-5 14 14"/><path d="M16 32l10 10 4 2 4 4 4 2 4-2 6-6"/><path d="M4 26l12 6M68 26l-10 10"/></svg>
    <div class="stat-num">11</div><div class="stat-label">COMPANY EXITS</div>
  </div>
  <div class="stat" style="left:858px">
    <svg width="72" height="72" viewBox="0 0 72 72" fill="none" stroke="#fff" stroke-width="2.2" stroke-linejoin="round"><path d="M22 6h28v18c0 10-6 16-14 16s-14-6-14-16z"/><path d="M22 12H12c0 10 4 16 12 18M50 12h10c0 10-4 16-12 18"/><path d="M36 40v10M28 50h16v6H28zM24 56h24v8H24z"/><path d="M36 14l3 6 6 1-4 4 1 6-6-3-6 3 1-6-4-4 6-1z"/></svg>
    <div class="stat-num">2</div><div class="stat-label">AWARDS WON</div>
  </div>
</section>

<section class="expertise">
  <div class="abs expertise-panel panel-pale"></div>
  <h2 class="abs serif big-title">Area of<br>Expertise</h2>
  <div class="service" style="left:588px;top:55px"><h3>NETWORK SUPPORT</h3><p>Help you build your network, introducing you to the right people in the right places.</p></div>
  <div class="service" style="left:880px;top:55px"><h3>REVENUE ACCELERATION</h3><p>Analyze your revenue streams, providing solutions for kickstarting your revenue</p></div>
  <div class="service" style="left:588px;top:219px"><h3>MERGERS &amp; ACQUSITIONS</h3><p>Facilitate a smooth mergers and acquisition process for the expansion of your business</p></div>
  <div class="service" style="left:878px;top:219px"><h3>INTEGRATION &amp; INCUBATION</h3><p>Providing training and guidance for startups looking to make their mark on the world.</p></div>
  <div class="service" style="left:596px;top:378px"><h3>RAISING CAPITAL</h3><p style="margin-left:-7px">Reach out to our extensive connections to raise vital capital for your startup.</p></div>
  <div class="service" style="left:882px;top:378px"><h3>MARKETING</h3><p style="margin-left:-2px">Consult on marketing process, strategies and implementation across your startup.</p></div>
</section>

<section class="who" role="img" aria-label="Business team reviewing documents at a laptop, under a pale blue tint">
  <h2 class="abs serif">Who We Are</h2>
  <div class="abs who-copy">
    <p>Torvella Capital is a venture capital studio firm based in Marlow Bay with a laser focus on raising solid capital for startups and helping businesses jumpstart their revenue.</p>
    <p>Founded in 2020 by investment expert Daniel Revaro, Torvella Capital combines proven experience in the venture capital field with a data-driven business analysis strategy to secure capital and reinforce revenue streams for startups and established businesses. Born from the idea that the best way to help founders thrive is to understand their strengths, their weaknesses, their ambitions and their needs - our specialists have been through the entire startup process themselves, and that experience forms our unique approach to business support.</p>
    <p>Daniel’s work in the sector has seen him take on the biggest and the best, working with iconic business figures to leave an indelible mark on the regional startup scene. He brings all of that expertise to the table at Torvella Capital, leading a dedicated team to support the finest international businesses to reach, break through and go beyond their potential.</p>
  </div>
  <div class="abs who-cta"><a class="link-cta">Let’s Work Together</a></div>
</section>

<section class="approach">
  <div class="abs approach-panel panel-pale"></div>
  <h2 class="abs serif big-title">Our<br>Approach</h2>
  <div class="abs approach-copy">
    <p>We’ve built our approach to helping your startup thrive based around three key developmental pillars that guarantee results for our partners.</p>
    <p>First pillar is expertise. We’ve built our firm on a bank of insights, knowledge and proficiencies honed over years of working with the biggest names in venture capitalism – that experience forms the backbone of every project, every pitch and every investment.</p>
    <p>Second pillar is collaboration. We believe that the best partnerships start with a combined and cooperative approach that benefits all parties every step of the way. We’ll always keep our partners up-to-date with our work using regular touchpoints and reports.</p>
    <p>Third and final pillar is trust. We know that our clients and our partners know their industry better than we do, so we trust their input and their ideas – pairing them up with our own business intelligence to guarantee success.</p>
  </div>
  <a class="abs approach-cta">Build With Us</a>
</section>

<section class="clients">
  <h2 class="abs serif">Our Clients</h2>
  <div class="client" style="left:69px;top:156px"><i></i>Velnori</div>
  <div class="client" style="left:212px;top:156px">Lumeqa</div>
  <div class="client" style="left:371px;top:156px"><i></i>urbanquill</div>
  <div class="client" style="left:541px;top:156px">Cirvanta</div>
  <div class="client" style="left:700px;top:156px"><i></i>Genorva</div>
  <div class="client" style="left:837px;top:156px">pelu</div>
  <div class="client" style="left:977px;top:156px">earthvine</div>
  <div class="client" style="left:69px;top:247px"><i></i>Vantrelo</div>
  <div class="client" style="left:217px;top:247px">lexbenda</div>
  <div class="client" style="left:380px;top:247px">brimwell</div>
  <div class="client" style="left:541px;top:247px"><i></i>Heliqen</div>
  <div class="client" style="left:700px;top:247px">TAVLO</div>
  <div class="client" style="left:837px;top:247px">thatroad</div>
  <div class="client" style="left:977px;top:247px">Homelark</div>
</section>

<section class="news">
  <h2 class="abs serif">Latest News</h2>
  <article class="post" style="left:85px">
    <h3>We’ve built our firm on a bank of insights, knowledge and proficiencies</h3>
    <div class="post-meta">10.12.2021<span>Auther Name</span></div>
    <p>Aenean imperdiet. Etiam ultricies nisi vel augue. Curabitur ullamcorper ultricies nisi. Nam eget dui. Etiam rhoncus. Maecenas tempus, tellus eget condimentum rhoncus, sem quam semper libero,</p>
    <a class="read-more">Read more</a>
  </article>
  <article class="post" style="left:439px">
    <h3>We believe that the best partnerships start with a combined and cooperative</h3>
    <div class="post-meta">10.12.2021<span>Auther Name</span></div>
    <p>Aenean imperdiet. Etiam ultricies nisi vel augue. Curabitur ullamcorper ultricies nisi. Nam eget dui. Etiam rhoncus. Maecenas tempus, tellus eget condimentum rhoncus, sem quam semper libero,</p>
    <a class="read-more">Read more</a>
  </article>
  <article class="post" style="left:788px">
    <h3>We know that our clients and our partners know their industry better</h3>
    <div class="post-meta">10.12.2021<span>Auther Name</span></div>
    <p>Aenean imperdiet. Etiam ultricies nisi vel augue. Curabitur ullamcorper ultricies nisi. Nam eget dui. Etiam rhoncus. Maecenas tempus, tellus eget condimentum rhoncus, sem quam semper libero,</p>
    <a class="read-more">Read more</a>
  </article>
</section>

<section class="newsletter">
  <h2 class="abs serif">Want to get up to date news?</h2>
  <h3 class="abs serif">Subscribe to Our Newsletter</h3>
  <div class="field" style="left:380px;top:148px;width:343px;height:35px">Your email</div>
  <div class="btn" style="left:732px;top:148px;width:88px;height:35px;background:#3b7cc6">SIGN UP</div>
</section>

<section class="contact">
  <h2 class="abs serif">Build With Us</h2>
  <p class="abs contact-intro">Please fill out the form to share your details and SUBMIT.<br>One of our representative will get back to you.</p>
  <div class="field" style="left:262px;top:198px;width:325px;height:34px">Your name</div>
  <div class="field" style="left:262px;top:253px;width:325px;height:34px">Your email</div>
  <div class="field" style="left:262px;top:309px;width:325px;height:34px">Your phone</div>
  <div class="field" style="left:613px;top:197px;width:325px;height:90px;align-items:flex-start;padding-top:11px">Type your message here ...</div>
  <div class="btn" style="left:614px;top:310px;width:188px;height:35px;background:var(--sky-bright)">SUBMIT</div>
  <div class="abs footer-rule"></div>
  <p class="abs copyright">Copyright © 2022 Torvella Capital.</p>
  <span class="social" style="left:837px"></span>
  <span class="social" style="left:874px"></span>
  <span class="social" style="left:911px"></span>
</section>

</body>
</html>
```